QRW Business Card Design

Business card design per the attached files.

Target Market(s)

Government and military officials, aerospace companies and aviation professionals

Industry/Entity Type

Business

```html
<!DOCTYPE html>
<html lang="en">
<head>
<meta charset="utf-8">
<title>QRW Business Card</title>
<link href="https://fonts.googleapis.com/css2?family=Lato:ital,wght@0,400;0,700;0,900;1,700&display=swap" rel="stylesheet">
<style>
  :root {
    --backdrop: #e9e7e4;
    --card-dark: #1c1c1d;
    --card-light: #ffffff;
    --emboss: #4a4a4b;
    --tagline: #454547;
    --ink: #111111;
    --accent: #3b7fc6;
    --globe-grey: #b9bbbe;
    --globe-blue: #2c4f9e;
  }
  * { margin: 0; padding: 0; box-sizing: border-box; }
  html, body {
    width: 1200px; height: 800px; overflow: hidden;
    background: var(--backdrop);
    font-family: "Lato", sans-serif;
  }
  .canvas { position: relative; width: 1200px; height: 800px; }

  .card {
    position: absolute;
    width: 494px; height: 288px;
    border-radius: 12px;
    box-shadow: 0 4px 14px rgba(0,0,0,0.18);
  }
  .card--front { left: 279px; top: 122px; background: var(--card-dark); }
  .card--back  { left: 278px; top: 428px; background: var(--card-light); overflow: hidden; }

  .front-brand {
    position: absolute; left: 0; right: 0; top: 124px;
    text-align: center;
    font-weight: 900; font-size: 32px; letter-spacing: 1px;
    line-height: 40px;
    color: var(--emboss);
  }
  .front-tagline {
    position: absolute; left: 0; right: 0; top: 220px;
    text-align: center;
    font-weight: 700; font-size: 13px; letter-spacing: 1.2px;
    color: var(--tagline);
  }

  .back-brand {
    position: absolute; left: 32px; top: 38px;
    font-weight: 900; font-size: 21px; line-height: 26px;
    color: var(--ink);
  }
  .back-division {
    position: absolute; right: 294px; top: 72px;
    font-weight: 700; font-style: italic; font-size: 12px; color: var(--ink);
  }
  .person-name {
    position: absolute; left: 30px; top: 115px;
    font-weight: 700; font-size: 17px; color: var(--accent);
  }
  .person-role {
    position: absolute; left: 30px; top: 139px;
    font-weight: 700; font-size: 11px; color: var(--ink);
  }
  .contact-list {
    position: absolute; left: 30px; top: 187px;
    list-style: none;
  }
  .contact-list li {
    display: flex; align-items: center;
    height: 15.5px;
    font-weight: 700; font-size: 11.5px; color: var(--ink);
    white-space: nowrap;
  }
  .contact-list svg { width: 11px; height: 11px; margin-right: 10px; fill: var(--accent); }

  .globe-art {
    position: absolute; left: 262px; top: 28px;
    width: 208px; height: 250px;
    border-radius: 50% 50% 48% 48%;
    background: radial-gradient(circle at 50% 55%, #e4e5e7 0%, var(--globe-grey) 62%, rgba(44,79,158,0.55) 100%);
  }
</style>
</head>
<body>
<main class="canvas">
  <section class="card card--front">
    <div class="front-brand">QRW Sky Systems</div>
    <div class="front-tagline">TRAIN - SIMULATE - CONNECT</div>
  </section>

  <section class="card card--back">
    <div class="back-brand">QRW Sky Systems</div>
    <div class="back-division">Polar Wing Ehf</div>
    <div class="person-name">Einar K. Thorvaldsson</div>
    <div class="person-role">Principal</div>
    <ul class="contact-list">
      <li><svg viewBox="0 0 24 24"><path d="M6.6 10.8a15 15 0 0 0 6.6 6.6l2.2-2.2a1 1 0 0 1 1-.25 11.4 11.4 0 0 0 3.6.6 1 1 0 0 1 1 1V20a1 1 0 0 1-1 1A17 17 0 0 1 3 4a1 1 0 0 1 1-1h3.5a1 1 0 0 1 1 1c0 1.25.2 2.45.6 3.6a1 1 0 0 1-.25 1z"/></svg>+354 555 0142</li>
      <li><svg viewBox="0 0 24 24"><path d="M7 1h10a2 2 0 0 1 2 2v18a2 2 0 0 1-2 2H7a2 2 0 0 1-2-2V3a2 2 0 0 1 2-2zm0 3v14h10V4zm5 15.5a1 1 0 1 0 0 2 1 1 0 0 0 0-2z"/></svg>+354 555 0187</li>
      <li><svg viewBox="0 0 24 24"><path d="M2 5h20v14H2zm2 2v.5l8 5 8-5V7z"/></svg>einar@qrw.is</li>
      <li><svg viewBox="0 0 24 24"><path d="M12 2a10 10 0 1 0 0 20 10 10 0 0 0 0-20zm0 2a8 8 0 0 1 7.7 6H15l-2-3-3 2 1 3-3 3v3.6A8 8 0 0 1 12 4z"/></svg>www.qrw.is</li>
      <li><svg viewBox="0 0 24 24"><path d="M12 1a7 7 0 0 0-7 7c0 5.3 7 15 7 15s7-9.7 7-15a7 7 0 0 0-7-7zm0 9.5A2.5 2.5 0 1 1 12 5.5a2.5 2.5 0 0 1 0 5z"/></svg>Sunnuvegur 12 105 Reykjavik Iceland</li>
    </ul>
    <div class="globe-art" role="img" aria-label="Illustration of a grey wireframe globe with blue flight paths and aircraft circling it"></div>
  </section>
</main>
</body>
</html>
```